Custom Wordpress Theme Needed

We need a custom Wordpress theme built with the following features:

1. Flat style design
2. Fully responsive - built for mobile and tablets first; bootstrap or other framework used
3. Flexible - comes with homepage layouts for portfolios, agencies, and magazines
4. Built in 'contact' and 'about us' styling
5. Pre-populated pages and content, including reusable images
6. Multiple slider options

We are completely open to your creativity as far as the overall design style is concerned, but some of our favorites are:
http://themes.plovaro.com/themeselector/?theme=TideBoard
http://www.kelmora.ru/flatmagazine/
http://quarnwellbox.com/wp/velta/intro/
http://theme.dovrask.net/second/

Most unique and in-depth style wins!

Reason: We need more designs!

Reason: Waiting on final submissions and revisions. Thanks!

```html
<!DOCTYPE html>
<html lang="en">
<head>
<meta charset="utf-8">
<title>Ken Marlow – Agency Home</title>
<link href="https://fonts.googleapis.com/css2?family=Roboto:ital,wght@0,300;0,400;0,500;1,400;1,500&display=swap" rel="stylesheet">
<style>
:root{
  --red:#c80000;
  --red-bright:#e32020;
  --header:#3a3a3a;
  --ink:#333;
  --text:#555;
  --muted:#888;
  --rule:#dcdcdc;
  --footer:#f2f2f2;
  --link:#1aa3d9;
  --white:#fff;
  --chirp:#55acee;
  --pin:#e0393e;
  --friend:#3b5998;
  --circle:#444;
}
*{box-sizing:border-box;margin:0;padding:0}
html,body{width:667px;height:1200px;overflow:hidden;background:var(--white)}
body{font-family:'Roboto',sans-serif;font-weight:400;color:var(--text);position:relative;font-synthesis:none}
.abs{position:absolute}
.page{position:relative;width:667px;height:1200px;overflow:hidden}

/* header */
.site-header{left:0;top:0;width:667px;height:56px;background:var(--header)}
.brand{left:73px;top:20px;font-size:17.5px;font-weight:500;color:var(--white);letter-spacing:.2px;line-height:20px}
.main-nav{left:206px;top:26px;display:flex;font-size:8px;color:#ddd;font-weight:300}
.main-nav span{padding:0 5px;border-left:1px solid #777;line-height:9px}
.main-nav span:first-child{border-left:0;padding-left:0}
.header-social{left:453px;top:28px;display:flex;gap:3px}
.header-social i{width:5px;height:5px;background:#eee;border-radius:50%;display:block}
.search{left:506px;top:25px;width:95px;height:12px;background:var(--white);font-size:6.5px;font-weight:300;color:#999;padding:2px 4px;line-height:8px}
.search svg{position:absolute;right:3px;top:2px}

/* hero */
.hero{left:0;top:56px;width:667px;height:261px;background:linear-gradient(90deg,#7fa9b3 0%,#1e1e22 18%,#2a2a2e 50%,#1e1e22 68%,#9cbac1 85%,#c9dade 100%)}
.slide-arrow{top:173px;width:26px;height:26px;border-radius:50%;background:var(--white);display:flex;align-items:center;justify-content:center}

/* services */
.services{left:0;top:317px;width:667px;height:168px;background:var(--red)}
.services h2{position:absolute;left:0;width:667px;top:13px;text-align:center;color:var(--white);font-size:13px;font-weight:500}
.service-thumb{top:42px;width:122px;height:88px;border:3px solid var(--white)}
.service-caption{top:141px;font-size:7.4px;font-weight:400;color:var(--white)}

/* section titles */
.section-title{font-size:13.5px;font-weight:300;color:var(--ink)}
.rule{height:1px;background:var(--rule)}
.vrule{width:1px;background:var(--rule)}

.article-thumb{width:122px;height:89px}
.link-badge{position:absolute;left:49px;top:33px;width:24px;height:24px;border-radius:50%;background:rgba(70,70,70,.75);display:flex;align-items:center;justify-content:center}
.article-flag{position:absolute;left:0;bottom:0;width:122px;height:28px;background:var(--red);color:var(--white);padding:4px 5px;font-size:6.5px;line-height:9px;font-weight:300}
.article-flag b{font-style:italic;font-weight:500;display:block}
.article-flag .go{position:absolute;right:6px;top:8px;width:11px;height:11px;border-radius:50%;background:var(--white)}

.pager{display:flex;gap:3px}
.pager i{width:10px;height:10px;border-radius:50%;background:#444;display:block}

.photo-thumb{width:74px;height:62px}
.video-thumb{width:75px;height:62px}
.play{position:absolute;left:30px;top:22px}
.entry{font-size:7.3px;line-height:13px;color:var(--text);font-weight:300;width:108px}
.entry b{font-weight:400;color:var(--ink);display:block}

/* sidebar */
.social-square{top:538px;width:19px;height:19px;display:flex;align-items:center;justify-content:center}
.social-square i{width:7px;height:7px;border:1.2px solid var(--white);border-radius:50%;display:block}
.tweet{font-size:7.3px;line-height:12px;color:var(--ink);font-weight:400;width:112px}
.tweet .url{color:var(--link);display:block;font-weight:300}
.tweet .time{color:var(--muted);display:block;font-weight:300}
.stars{display:flex;gap:1px;margin-top:3px}

/* footer */
.site-footer{left:0;top:1000px;width:667px;height:200px;background:var(--footer)}
.footer-title{top:1021px;font-size:9.6px;font-weight:400;color:#555}
.footer-links{top:1056px;font-size:7.6px;line-height:16.8px;font-weight:300;color:#555}
.newsletter-text{left:345px;top:1052px;width:122px;font-size:7.3px;line-height:16.8px;font-weight:300;color:#666;text-align:justify}
.field{left:345px;width:123px;height:15px;background:var(--white);border:1px solid #e2e2e2;font-size:7.2px;font-weight:300;color:#666;padding:2px 7px}
.subscribe{left:414px;top:1126px;width:54px;height:13px;border-radius:7px;background:var(--red-bright);color:var(--white);font-size:7.6px;font-weight:500;text-align:center;line-height:13px}
.connect-row{left:522px;font-size:7.6px;font-weight:300;color:#555;display:flex;align-items:center;width:72px;justify-content:space-between}
.connect-row i{width:15px;height:15px;border-radius:50%;border:1px solid #ddd;background:#fafafa;display:block}
.copyright{left:0;top:1169px;width:667px;text-align:center;font-size:7.3px;font-weight:400;color:#555}
</style>
</head>
<body>
<div class="page">

  <header class="site-header abs">
    <div class="brand abs">KEN MARLOW</div>
    <nav class="main-nav abs"><span>Home</span><span>About Us</span><span>Services</span><span>Testimonials</span><span>Contact Us</span></nav>
    <div class="header-social abs" aria-label="Social links"><i title="Chirplane"></i><i title="Friendwall"></i><i title="Clipcast"></i><i title="Feed"></i><i title="Circlespace"></i></div>
    <div class="search abs">Search
      <svg width="8" height="8" viewBox="0 0 8 8"><circle cx="3.2" cy="3.2" r="2.3" fill="none" stroke="#444" stroke-width="1"/><line x1="5" y1="5" x2="7.5" y2="7.5" stroke="#444" stroke-width="1.2"/></svg>
    </div>
  </header>

  <section class="hero abs" role="img" aria-label="Businessman in a dark suit holding a tablet, office windows behind"></section>
  <div class="slide-arrow abs" style="left:40px"><svg width="10" height="12" viewBox="0 0 10 12"><path d="M7 1L2 6l5 5" fill="none" stroke="#333" stroke-width="2"/></svg></div>
  <div class="slide-arrow abs" style="left:601px"><svg width="10" height="12" viewBox="0 0 10 12"><path d="M3 1l5 5-5 5" fill="none" stroke="#333" stroke-width="2"/></svg></div>

  <section class="services abs">
    <h2>Our Services</h2>
    <div class="service-thumb abs" style="left:66px;background:linear-gradient(135deg,#cfd6dc,#8aa3b8)" role="img" aria-label="Smiling team of colleagues"></div>
    <div class="service-thumb abs" style="left:199px;background:linear-gradient(135deg,#aab4bd,#4f5862)" role="img" aria-label="Business meeting around a table"></div>
    <div class="service-thumb abs" style="left:334px;background:linear-gradient(135deg,#3a8fd0,#1b4f8a)" role="img" aria-label="Head made of puzzle pieces among digital icons"></div>
    <div class="service-thumb abs" style="left:466px;background:linear-gradient(135deg,#f4f4f2,#c9c6bd)" role="img" aria-label="Man drawing charts on a whiteboard"></div>
    <div class="service-caption abs" style="left:64px">Neque porro quisquam est</div>
    <div class="service-caption abs" style="left:198px">Neque porro quisquam est</div>
    <div class="service-caption abs" style="left:333px">Neque porro quisquam est</div>
    <div class="service-caption abs" style="left:466px">Neque porro quisquam est</div>
  </section>

  <!-- articles -->
  <h3 class="section-title abs" style="left:73px;top:504px">Latest Agency Articles</h3>
  <div class="rule abs" style="left:70px;top:526px;width:392px"></div>
  <div class="vrule abs" style="left:473px;top:502px;height:476px"></div>

  <div class="article-thumb abs" style="left:70px;top:538px;background:linear-gradient(180deg,#5a9fd8,#b9d6ee 60%,#6d7f8c)" role="img" aria-label="Photographer with a camera against the sky">
    <div class="article-flag"><b>Ed ut perspiciatis unde omnis</b>Remque laudantium<span class="go"></span></div>
  </div>
  <div class="article-thumb abs" style="left:206px;top:538px;background:linear-gradient(135deg,#d8e4ec,#5f7d95)" role="img" aria-label="Glass office tower"><span class="link-badge"><svg width="12" height="12" viewBox="0 0 12 12"><rect x="1" y="4" width="6" height="4" rx="2" fill="none" stroke="#fff" stroke-width="1.2" transform="rotate(-45 6 6)"/><rect x="5" y="4" width="6" height="4" rx="2" fill="none" stroke="#fff" stroke-width="1.2" transform="rotate(-45 6 6)"/></svg></span></div>
  <div class="article-thumb abs" style="left:340px;top:538px;background:linear-gradient(135deg,#3a3530,#e9e2d6)" role="img" aria-label="Hands reviewing financial charts"><span class="link-badge"><svg width="12" height="12" viewBox="0 0 12 12"><rect x="1" y="4" width="6" height="4" rx="2" fill="none" stroke="#fff" stroke-width="1.2" transform="rotate(-45 6 6)"/><rect x="5" y="4" width="6" height="4" rx="2" fill="none" stroke="#fff" stroke-width="1.2" transform="rotate(-45 6 6)"/></svg></span></div>
  <div class="article-thumb abs" style="left:72px;top:655px;background:linear-gradient(180deg,#7cc1e4,#c8a58b)" role="img" aria-label="Group of raised thumbs up"><span class="link-badge"><svg width="12" height="12" viewBox="0 0 12 12"><rect x="1" y="4" width="6" height="4" rx="2" fill="none" stroke="#fff" stroke-width="1.2" transform="rotate(-45 6 6)"/><rect x="5" y="4" width="6" height="4" rx="2" fill="none" stroke="#fff" stroke-width="1.2" transform="rotate(-45 6 6)"/></svg></span></div>
  <div class="article-thumb abs" style="left:206px;top:655px;background:linear-gradient(135deg,#d9d7b0,#6e5a44)" role="img" aria-label="Hands holding a phone"><span class="link-badge"><svg width="12" height="12" viewBox="0 0 12 12"><rect x="1" y="4" width="6" height="4" rx="2" fill="none" stroke="#fff" stroke-width="1.2" transform="rotate(-45 6 6)"/><rect x="5" y="4" width="6" height="4" rx="2" fill="none" stroke="#fff" stroke-width="1.2" transform="rotate(-45 6 6)"/></svg></span></div>
  <div class="article-thumb abs" style="left:340px;top:655px;background:radial-gradient(circle at 55% 45%,#6fa8ff,#12306b 70%)" role="img" aria-label="Glowing network of connected nodes"><span class="link-badge"><svg width="12" height="12" viewBox="0 0 12 12"><rect x="1" y="4" width="6" height="4" rx="2" fill="none" stroke="#fff" stroke-width="1.2" transform="rotate(-45 6 6)"/><rect x="5" y="4" width="6" height="4" rx="2" fill="none" stroke="#fff" stroke-width="1.2" transform="rotate(-45 6 6)"/></svg></span></div>

  <!-- photos -->
  <h3 class="section-title abs" style="left:74px;top:769px">Photos</h3>
  <div class="pager abs" style="left:209px;top:773px"><i></i><i></i></div>
  <div class="rule abs" style="left:70px;top:794px;width:170px"></div>
  <div class="vrule abs" style="left:260px;top:760px;height:218px"></div>
  <div class="photo-thumb abs" style="left:78px;top:811px;background:linear-gradient(90deg,#222,#777,#222)" role="img" aria-label="Star trophy on a stage"></div>
  <div class="photo-thumb abs" style="left:160px;top:811px;background:linear-gradient(180deg,#f2f2f2,#3b3d45)" role="img" aria-label="Business team standing together"></div>
  <div class="photo-thumb abs" style="left:78px;top:886px;background:linear-gradient(135deg,#e33,#f2c94c,#2a8fd0,#333)" role="img" aria-label="Colour swatches and print samples"></div>
  <div class="photo-thumb abs" style="left:160px;top:886px;background:linear-gradient(135deg,#f4f4f4,#d8b98e)" role="img" aria-label="Woman in front of sketched diagrams"></div>

  <!-- videos -->
  <h3 class="section-title abs" style="left:273px;top:769px">Featured Videos</h3>
  <div class="pager abs" style="left:438px;top:773px"><i></i><i></i></div>
  <div class="rule abs" style="left:271px;top:794px;width:191px"></div>
  <div class="video-thumb abs" style="left:275px;top:810px;background:linear-gradient(180deg,#8fb8e0,#cfd9df 55%,#5c6066)" role="img" aria-label="Road with yellow direction signs">
    <svg class="play" width="16" height="18" viewBox="0 0 16 18"><path d="M1 1l14 8-14 8z" fill="#fff" fill-opacity=".85"/></svg>
  </div>
  <div class="entry abs" style="left:357px;top:812px"><b>Ed ut perspiciatis unde omnis</b>Remque laudantium, totam rem aperiam, eaque ipsa quae ab illo inventore veritatis et</div>
  <div class="video-thumb abs" style="left:275px;top:884px;background:radial-gradient(circle at 45% 45%,#7fb2ea,#0f2d5c 70%)" role="img" aria-label="Glowing light bulb">
    <svg class="play" width="16" height="18" viewBox="0 0 16 18"><path d="M1 1l14 8-14 8z" fill="#fff" fill-opacity=".85"/></svg>
  </div>
  <div class="entry abs" style="left:357px;top:893px"><b>Nemo enim ipsam voluptatem</b>Quia voluptas sit aspernatur aut odit aut fugit, sed quia</div>

  <!-- sidebar -->
  <h3 class="section-title abs" style="left:484px;top:504px">Social Networks</h3>
  <div class="rule abs" style="left:482px;top:526px;width:113px"></div>
  <a class="social-square abs" style="left:484px;background:var(--chirp)" aria-label="Chirplane" title="Chirplane"><i></i></a>
  <a class="social-square abs" style="left:512px;background:var(--pin)" aria-label="Pinboardly" title="Pinboardly"><i></i></a>
  <a class="social-square abs" style="left:540px;background:var(--friend)" aria-label="Friendwall" title="Friendwall"><i></i></a>
  <a class="social-square abs" style="left:568px;background:var(--circle)" aria-label="Circlespace" title="Circlespace"><i></i></a>

  <h3 class="section-title abs" style="left:485px;top:580px">Recent Tweets</h3>
  <div class="rule abs" style="left:484px;top:602px;width:111px"></div>
  <div class="tweet abs" style="left:486px;top:608px">Hostwell is not good.<span class="time">about 5 days ago</span></div>
  <div class="tweet abs" style="left:486px;top:646px">New Plovaro gallery site to enjoy: Tide In Front<span class="url">http://t.co/Qx8pLm2RaK</span><span class="time">about 5 days ago</span></div>
  <div class="tweet abs" style="left:486px;top:716px">New Plovaro gallery site to enjoy: Velmora Kite<span class="url">http://t.co/ZbW4nTeVq</span><span class="time">5 about 5 days ago</span></div>

  <h3 class="section-title abs" style="left:485px;top:791px">Client Ratings</h3>
  <div class="rule abs" style="left:484px;top:813px;width:111px"></div>
  <div class="entry abs" style="left:486px;top:822px;width:110px"><b>Ed ut perspiciatis unde omnis</b>Remque laudantium, totam rem aperiam, eaque ipsa quae ab illo inventore veritatis et
    <div class="stars">
      <svg width="52" height="10" viewBox="0 0 52 10">
        <g fill="#e01b1b"><path id="st" d="M5 0l1.5 3.2 3.5.4-2.6 2.4.7 3.5L5 7.8 1.9 9.5l.7-3.5L0 3.6l3.5-.4z"/><use href="#st" x="10.5"/><use href="#st" x="21"/><use href="#st" x="31.5"/></g>
        <use href="#st" x="42" fill="#555"/>
      </svg>
    </div>
  </div>
  <div class="entry abs" style="left:486px;top:903px;width:110px"><b>Nemo enim ipsam voluptatem</b>Quia voluptas sit aspernatur aut odit aut fugit, sed quia
    <div class="stars">
      <svg width="52" height="10" viewBox="0 0 52 10">
        <g fill="#e01b1b"><path id="st2" d="M5 0l1.5 3.2 3.5.4-2.6 2.4.7 3.5L5 7.8 1.9 9.5l.7-3.5L0 3.6l3.5-.4z"/><use href="#st2" x="10.5"/><use href="#st2" x="21"/><use href="#st2" x="31.5"/></g>
        <use href="#st2" x="42" fill="#555"/>
      </svg>
    </div>
  </div>

  <!-- footer -->
  <footer class="site-footer abs"></footer>
  <div class="footer-title abs" style="left:76px">Quick Links</div>
  <div class="footer-title abs" style="left:210px">Support Links</div>
  <div class="footer-title abs" style="left:345px">Newsletter SignUp</div>
  <div class="footer-title abs" style="left:522px">Connect With Us</div>
  <div class="footer-links abs" style="left:76px">Home<br>About Us<br>Services<br>Solutions<br>Contact Us</div>
  <div class="footer-links abs" style="left:210px">Legal Notice<br>Privacy Policy<br>Terms &amp; Conditions<br>Help</div>
  <div class="newsletter-text abs">Sign-up for our daily emails by entering your information below:</div>
  <div class="field abs" style="top:1082px">Name</div>
  <div class="field abs" style="top:1105px">Enter Your E-Mail ID</div>
  <div class="subscribe abs">Subscribe</div>
  <div class="connect-row abs" style="top:1054px"><i></i>Chirplane</div>
  <div class="connect-row abs" style="top:1075px"><i></i>Friendwall</div>
  <div class="connect-row abs" style="top:1096px"><i></i>Workgrid</div>
  <div class="copyright abs">Copyright ©2013 &nbsp;Company Name &nbsp;&nbsp;- All rights reserved</div>

</div>
</body>
</html>
```